Professional Business Card - TWO SIDES

I need a new business card design to be used by myself and my employees. I would like a professional card and for the front I thought I would like a dark blue thatch with our logo in a raised gold foil on top of it. On the other side I would like name, position, and contact info. I've uploaded our old design for an example of the info used.

Target Market(s)

Business Clients

Industry/Entity Type

CPA Firm

Contact Information for Business Card

Logo, Name, Title, Address, Phone Numbers, Website address, Email Address

Font styles to use
Serif
Sans Serif

Colors
0054AA
0677BA
7BADD7
CADEEF
E8F1F8
0094D4
00A9DD
6FCCEA
C7EBF8
E9F6FB

Requirements
Must have
• Modern Professional Look
Nice to have
• Logo in Gold Foil or ability to have is raised. I like our logo in a single color
Should not have
• I've uploaded old business card

```html
<!DOCTYPE html>
<html lang="en">
<head>
<meta charset="utf-8">
<title>Harlow Lane CPA – Business Card</title>
<link rel="stylesheet" href="https://fonts.googleapis.com/css2?family=Arimo:wght@400;700&display=swap">
<style>
  :root {
    --navy: #0b3a6e;
    --navy-deep: #082f5c;
    --lime: #a9cf3a;
    --white: #ffffff;
    --stage: #2a2a2a;
    --rule: #6f8fb4;
  }
  * { box-sizing: border-box; margin: 0; padding: 0; }
  html, body { width: 1200px; height: 900px; overflow: hidden; }
  body {
    background: var(--stage);
    font-family: "Arimo", Arial, sans-serif;
    position: relative;
  }
  .card {
    position: absolute;
    left: 260px;
    width: 680px;
    height: 389px;
    border-radius: 26px;
    overflow: hidden;
    box-shadow: 0 14px 30px rgba(0,0,0,.45);
  }
  .card--info { top: 40px; background: var(--white); }
  .card--brand {
    top: 471px;
    background: linear-gradient(135deg, #0d4279 0%, var(--navy-deep) 100%);
  }

  /* info side */
  .info-band {
    position: absolute; left: 0; right: 0; top: 178px; height: 146px;
    background: var(--navy);
  }
  .info-stripe {
    position: absolute; left: 0; right: 0; top: 330px; bottom: 0;
    background: var(--lime);
    display: flex; align-items: center; justify-content: center;
    color: var(--white); font-size: 17px;
  }
  .brand {
    position: absolute; text-align: center; color: var(--navy);
  }
  .brand__name {
    font-weight: 700; font-size: 46px; letter-spacing: 1px; line-height: 1;
    text-transform: uppercase;
  }
  .brand__tag {
    font-weight: 700; font-size: 13px; letter-spacing: 4.6px; margin-top: 6px;
    text-transform: uppercase;
  }
  .card--info .brand { left: 0; right: 0; top: 62px; }

  .person {
    position: absolute; right: 360px; top: 206px; text-align: right; color: var(--white);
  }
  .person__name { font-weight: 700; font-size: 26px; }
  .person__role { font-size: 16px; margin-top: 4px; }
  .divider {
    position: absolute; left: 338px; top: 200px; width: 1px; height: 80px; background: var(--rule);
  }
  .contacts {
    position: absolute; left: 360px; top: 198px; list-style: none; color: var(--white); font-size: 17px;
  }
  .contacts li { display: flex; align-items: center; gap: 10px; height: 28px; }
  .contacts svg { width: 15px; height: 15px; flex: none; }

  /* brand side */
  .card--brand .brand { right: 50px; top: 230px; color: var(--white); text-align: left; }
  .card--brand .brand__name { font-size: 58px; }
  .card--brand .brand__tag { font-size: 16px; letter-spacing: 5.4px; }
</style>
</head>
<body>
  <section class="card card--info" aria-label="Card back with contact details">
    <div class="brand">
      <div class="brand__name">Harlow Lane</div>
      <div class="brand__tag">Certified Public Accountants</div>
    </div>
    <div class="info-band"></div>
    <div class="person">
      <div class="person__name">Daniel Reyes</div>
      <div class="person__role">Manager</div>
    </div>
    <div class="divider"></div>
    <ul class="contacts">
      <li>
        <svg viewBox="0 0 16 16" fill="#fff"><path d="M3.6 1.5l2.2 2.6-1.3 1.6c.9 2 2.4 3.6 4.5 4.6l1.6-1.3 2.7 2.2-1.2 2.2C7 13.3 2.7 9 1.6 3l2-1.5z"/></svg>
        555-014-2100
      </li>
      <li>
        <svg viewBox="0 0 16 16" fill="none" stroke="#fff" stroke-width="1.5"><rect x="1.5" y="3.5" width="13" height="9"/><path d="M1.5 3.5L8 9l6.5-5.5"/></svg>
        daniel@harlowlane.com
      </li>
      <li>
        <svg viewBox="0 0 16 16" fill="none" stroke="#fff" stroke-width="1.3"><circle cx="8" cy="8" r="6.5"/><ellipse cx="8" cy="8" rx="3" ry="6.5"/><path d="M1.5 8h13M3 4.5h10M3 11.5h10"/></svg>
        www.harlowlane.com
      </li>
    </ul>
    <div class="info-stripe">Your address, city, state, ZIP 0000</div>
  </section>

  <section class="card card--brand" aria-label="Card front with firm name">
    <div class="brand">
      <div class="brand__name">Harlow Lane</div>
      <div class="brand__tag">Certified Public Accountants</div>
    </div>
  </section>
</body>
</html>
```